Biz cards and stationary design
for Harbor Pathways
Project: Biz cards and stationary design
Biz cards and stationary design  - Consulting
Creative Brief
Professional
Tessa R Windrow
President
27816 Dovelin Court Fairbrook, OR 97321
tessa.windrow@harborpathways-example.com
http://www.harborpathways-example.com

```html
<!DOCTYPE html>
<html lang="en">
<head>
<meta charset="utf-8">
<title>Harbor Pathways — Business Cards and Stationery</title>
<link href="https://fonts.googleapis.com/css2?family=Cinzel:wght@700&family=Open+Sans:wght@400;600&display=swap" rel="stylesheet">
<style>
:root{
  --backdrop:#d4b183;
  --paper:#ffffff;
  --flap:#f6f6f6;
  --wine:#7e1419;
  --red:#b0242b;
  --gold:#f4b21f;
  --orange:#e9771c;
  --ink:#444;
  --muted:#888;
  --rule:#bdbdbd;
  --line:#dcdcdc;
}
*{box-sizing:border-box;margin:0;padding:0}
html,body{width:1200px;height:679px;overflow:hidden}
body{background:var(--backdrop);font-family:"Open Sans",Arial,sans-serif;color:var(--ink);position:relative}
.sheet,.card,.envelope{position:absolute;background:var(--paper);box-shadow:0 3px 8px rgba(0,0,0,.3);overflow:hidden}
.label{position:absolute;font-size:7px;line-height:9px;color:#3a2a1a;text-align:center;font-weight:600}
.wave{position:absolute;left:0;top:0;width:100%;display:block}
.brand{font-family:"Cinzel",Georgia,serif;font-weight:700;color:var(--red);white-space:nowrap;display:flex;align-items:center;gap:4px;line-height:1}
.brand .dot{width:6px;height:6px;border-radius:50%;background:var(--gold);display:inline-block;flex:none}
.footer{position:absolute;left:0;right:0;bottom:14px;text-align:center;font-size:5.5px;line-height:1.6;color:var(--muted)}

/* business cards */
.card{top:41px;width:149px;height:79px}
.card-info{left:504px}
.card-logo{left:672px}
.card-wine{left:838px;background:linear-gradient(135deg,var(--red),var(--wine))}
.card-gold{left:1003px;background:radial-gradient(circle at 50% 50%,#ffe58a,var(--gold) 55%,var(--orange))}
.card .brand{position:absolute;left:50%;top:50%;transform:translate(-50%,-50%);font-size:9px}
.card-wine .brand{color:#fff}
.card-gold .brand{color:var(--wine)}
.card-info .brand{left:50%;top:24px;transform:translateX(-50%);font-size:8px}
.card-info .contact{position:absolute;left:8px;top:42px;font-size:4.3px;line-height:1.5;color:var(--ink)}
.card-info .contact b{font-weight:600;color:var(--wine)}
.card-info .web{position:absolute;right:8px;top:42px;font-size:4.3px;line-height:1.5;color:var(--ink);text-align:right}

/* fax cover */
.fax{left:29px;top:154px;width:350px;height:496px}
.fax-title{position:absolute;left:18px;top:79px;font-size:10px;line-height:12px;font-weight:600;color:var(--wine)}
.fax-table{position:absolute;left:19px;top:93px;width:312px;border-collapse:collapse;font-size:6.5px}
.fax-table td{border:1px solid var(--rule);height:21px;padding:0 4px}
.fax-table .key{width:38px}
.fax-checks{position:absolute;left:19px;top:189px;display:flex;gap:17px;font-size:6px;line-height:8px}
.fax-checks span::before{content:"";display:inline-block;width:6px;height:6px;border:1px solid var(--muted);margin-right:3px;vertical-align:-1px}

/* letterhead */
.letterhead{left:401px;top:154px;width:350px;height:496px}
.letterhead .brand{position:absolute;left:50%;transform:translateX(-50%);top:74px;font-size:15px}

/* envelopes */
.env-front{left:773px;top:154px;width:362px;height:187px}
.env-front .brand{position:absolute;right:22px;top:68px;font-size:14px}
.env-front .return{position:absolute;right:22px;top:88px;font-size:5.5px;color:var(--muted);text-align:right;line-height:1.5}
.env-back svg{position:absolute;inset:0;width:100%;height:100%}
.env-back-1{left:773px;top:362px;width:362px;height:120px}
.env-back-2{left:792px;top:456px;width:372px;height:163px}
.env-back-2 .brand{position:absolute;left:50%;transform:translateX(-50%);top:20px;font-size:10px;color:#fff}
</style>
</head>
<body>

<!-- business cards -->
<div class="card card-info">
  <svg class="wave" viewBox="0 0 149 22" preserveAspectRatio="none" height="22"><path d="M0 0H149V8C108 20 54 4 0 16Z" fill="var(--red)"/><path d="M0 16C54 4 108 20 149 8V10C108 22 54 6 0 18Z" fill="var(--gold)"/></svg>
  <div class="brand"><i class="dot"></i>Harbor Pathways</div>
  <div class="contact"><b>Tessa R Windrow</b><br>President<br>27816 Dovelin Court<br>Fairbrook, OR 97321<br>(541) 555-0148</div>
  <div class="web">tessa.windrow@<br>harborpathways-example.com<br>www.harborpathways-example.com</div>
</div>
<div class="card card-logo"><div class="brand"><i class="dot"></i>Harbor Pathways</div></div>
<div class="card card-wine"><div class="brand"><i class="dot"></i>Harbor Pathways</div></div>
<div class="card card-gold"><div class="brand"><i class="dot"></i>Harbor Pathways</div></div>

<!-- fax cover -->
<div class="label" style="left:29px;top:142px;width:350px">Fax Cover</div>
<div class="sheet fax">
  <svg class="wave" viewBox="0 0 350 72" preserveAspectRatio="none" height="72"><path d="M0 0H350V30C256 72 128 20 0 54Z" fill="var(--wine)"/><path d="M0 54C128 20 256 72 350 30V34C256 76 128 24 0 58Z" fill="var(--gold)"/></svg>
  <div class="fax-title">FAX</div>
  <table class="fax-table">
    <tr><td class="key">To:</td><td></td><td class="key">From:</td><td></td></tr>
    <tr><td class="key">Fax:</td><td></td><td class="key">Pages:</td><td></td></tr>
    <tr><td class="key">Phone:</td><td></td><td class="key">Date:</td><td></td></tr>
    <tr><td class="key">Re:</td><td></td><td class="key">CC:</td><td></td></tr>
  </table>
  <div class="fax-checks"><span>Urgent</span><span>For Review</span><span>Please Comment</span><span>Please Reply</span><span>Please Recycle</span></div>
  <div class="footer">27816 Dovelin Court Fairbrook, OR 97321<br>(541) 555-0148 &nbsp;·&nbsp; tessa.windrow@harborpathways-example.com &nbsp;·&nbsp; http://www.harborpathways-example.com</div>
</div>

<!-- letterhead -->
<div class="label" style="left:401px;top:142px;width:350px">Letterhead</div>
<div class="sheet letterhead">
  <svg class="wave" viewBox="0 0 350 72" preserveAspectRatio="none" height="72"><path d="M0 0H350V30C256 72 128 20 0 54Z" fill="var(--wine)"/><path d="M0 54C128 20 256 72 350 30V34C256 76 128 24 0 58Z" fill="var(--gold)"/></svg>
  <div class="brand"><i class="dot"></i>Harbor Pathways</div>
  <div class="footer">27816 Dovelin Court Fairbrook, OR 97321<br>(541) 555-0148 &nbsp;·&nbsp; tessa.windrow@harborpathways-example.com &nbsp;·&nbsp; http://www.harborpathways-example.com</div>
</div>

<!-- envelope front -->
<div class="label" style="left:773px;top:142px;width:362px">Envelopes (Front)</div>
<div class="envelope env-front">
  <svg class="wave" viewBox="0 0 362 56" preserveAspectRatio="none" height="56"><path d="M0 0H362V22C260 56 126 12 0 40Z" fill="var(--wine)"/><path d="M0 40C126 12 260 56 362 22V26C260 60 126 16 0 44Z" fill="var(--gold)"/></svg>
  <div class="brand"><i class="dot"></i>Harbor Pathways</div>
  <div class="return">27816 Dovelin Court<br>Fairbrook, OR 97321</div>
</div>

<!-- envelope back, option 1 -->
<div class="label" style="left:773px;top:352px;width:362px">Envelopes (Back) Option 1</div>
<div class="envelope env-back env-back-1">
  <svg viewBox="0 0 362 120" preserveAspectRatio="none"><path d="M0 0H362L181 58Z" fill="var(--flap)" stroke="var(--line)"/><path d="M0 120L150 50M362 120L212 50" stroke="var(--line)"/></svg>
</div>

<!-- envelope back, option 2 -->
<div class="label" style="left:792px;top:445px;width:372px">Envelopes (Back) Option 2</div>
<div class="envelope env-back env-back-2">
  <svg viewBox="0 0 372 163" preserveAspectRatio="none"><defs><linearGradient id="flap" x1="0" y1="0" x2="0" y2="1"><stop offset="0" stop-color="var(--red)"/><stop offset="1" stop-color="var(--wine)"/></linearGradient></defs><path d="M0 163L156 70M372 163L216 70" stroke="var(--line)"/><path d="M0 0L186 78L372 0V4L186 83L0 4Z" fill="var(--gold)"/><path d="M0 0H372L186 78Z" fill="url(#flap)"/></svg>
  <div class="brand"><i class="dot"></i>Harbor Pathways</div>
</div>

</body>
</html>
```